New Zealand Export company needs business cards

We need new business cards to match our new logo for a company based in New Zealand who deal specifically with the Pacific Islands. We source, consolidate and ship products out of New Zealand to the Pacific Islands. Will attach our old ones and also new logo.
Would like the Islands we deal with and the areas of work we have access to, to be included on the business cards.

Contact Information for Business Card

T +64 9 571 3048
F +64 9 571 6285
12-18 Kowhai Lane, Harbourvale, 9071
PO Box 814, Harbourvale, Northland 9072, New Zealand
www.falconfreight.example.nz
E sales@falconfreight.example.nz

Font styles to use
Sans Serif

Colors
85abd2
33a6d7
ffffff

Requirements
Must have
• A company of PWM

```html
<!DOCTYPE html>
<html lang="en">
<head>
<meta charset="utf-8">
<title>Falcon Freight business cards</title>
<link rel="stylesheet" href="https://fonts.googleapis.com/css2?family=Montserrat:wght@400;500;700;800&display=swap">
<style>
  :root {
    --backdrop: #24272c;
    --brand-blue: #175bb0;
    --brand-blue-deep: #0f4c9c;
    --accent-sky: #33a6d7;
    --soft-blue: #85abd2;
    --paper: #ffffff;
  }
  * { box-sizing: border-box; margin: 0; padding: 0; }
  html, body {
    width: 1200px; height: 900px; overflow: hidden;
    background: var(--backdrop);
    font-family: "Montserrat", sans-serif;
  }
  .canvas {
    width: 1200px; height: 900px;
    display: flex; align-items: center; justify-content: center; gap: 50px;
  }
  .card {
    position: relative;
    width: 540px; height: 310px;
    border-radius: 4px;
    overflow: hidden;
    box-shadow: 0 12px 30px rgba(0,0,0,0.45);
  }
  /* front */
  .card--front { background: var(--paper); }
  .card__wave { position: absolute; inset: 0; width: 100%; height: 100%; }
  .brand {
    position: absolute; display: flex; align-items: center; gap: 10px;
    font-weight: 800; letter-spacing: 0.04em; text-transform: uppercase;
  }
  .brand__mark { width: 26px; height: 26px; }
  .card--front .brand { top: 28px; left: 30px; color: var(--brand-blue); font-size: 22px; }
  .card--front .brand__mark { background: var(--brand-blue); }
  .contact {
    position: absolute; right: 24px; top: 156px;
    text-align: right; color: var(--paper);
    font-size: 11px; line-height: 15px; font-weight: 500;
  }
  .contact__name { color: var(--accent-sky); font-weight: 700; font-size: 12px; letter-spacing: 0.03em; }
  .contact__role { margin-bottom: 1px; }
  .contact__row { display: flex; justify-content: flex-end; align-items: center; gap: 7px; }
  .contact__icon { width: 11px; height: 11px; fill: var(--soft-blue); flex: none; }
  .contact__address { margin-top: 2px; padding-right: 18px; }
  /* back */
  .card--back {
    background: linear-gradient(135deg, #1a64bd 0%, var(--brand-blue) 50%, var(--brand-blue-deep) 100%);
    display: flex; align-items: center; justify-content: center;
  }
  .card--back .brand { position: static; color: var(--paper); font-size: 26px; }
  .card--back .brand__mark { background: var(--paper); width: 30px; height: 30px; }
</style>
</head>
<body>
<main class="canvas">
  <section class="card card--front" aria-label="Business card front">
    <svg class="card__wave" viewBox="0 0 540 310" preserveAspectRatio="none" aria-hidden="true">
      <path d="M0,236 C150,262 250,205 340,150 C420,102 480,78 540,70 L540,310 L0,310 Z" fill="var(--brand-blue)"/>
      <path d="M20,200 C160,250 250,190 335,137 C415,88 480,62 540,55" fill="none" stroke="var(--accent-sky)" stroke-width="7"/>
    </svg>
    <div class="brand"><span class="brand__mark"></span>Falcon Freight</div>
    <div class="contact">
      <div class="contact__name">LENA HARTLEY</div>
      <div class="contact__role">Sales Manager</div>
      <div class="contact__row">+64 9 571 3048
        <svg class="contact__icon" viewBox="0 0 24 24"><path d="M6.6 10.8a15 15 0 0 0 6.6 6.6l2.2-2.2c.3-.3.7-.4 1-.2 1.1.4 2.3.6 3.6.6.6 0 1 .4 1 1V20c0 .6-.4 1-1 1A17 17 0 0 1 3 4c0-.6.4-1 1-1h3.5c.6 0 1 .4 1 1 0 1.3.2 2.5.6 3.6.1.3 0 .7-.2 1z"/></svg>
      </div>
      <div class="contact__row">+64 9 571 6285
        <svg class="contact__icon" viewBox="0 0 24 24"><path d="M6 2h10v6H6zM3 9h18v10h-4v3H7v-3H3zm6 7v4h6v-4z"/></svg>
      </div>
      <div class="contact__row">www.falconfreight.example.nz
        <svg class="contact__icon" viewBox="0 0 24 24"><path d="M12 2a10 10 0 1 0 0 20 10 10 0 0 0 0-20zm6.9 6h-3a15 15 0 0 0-1.3-3.8A8 8 0 0 1 18.9 8zM12 4c.8 1.2 1.5 2.5 1.9 4h-3.8c.4-1.5 1.1-2.8 1.9-4zM4.3 14a8 8 0 0 1 0-4h3.4a16 16 0 0 0 0 4zm.8 2h3a15 15 0 0 0 1.3 3.8A8 8 0 0 1 5.1 16zm3-8h-3a8 8 0 0 1 4.3-3.8C8.8 5.5 8.4 6.7 8.1 8zM12 20c-.8-1.2-1.5-2.5-1.9-4h3.8c-.4 1.5-1.1 2.8-1.9 4zm2.3-6H9.7a14 14 0 0 1 0-4h4.6a14 14 0 0 1 0 4zm.3 5.8c.6-1.2 1-2.4 1.3-3.8h3a8 8 0 0 1-4.3 3.8zm1.7-5.8a16 16 0 0 0 0-4h3.4a8 8 0 0 1 0 4z"/></svg>
      </div>
      <div class="contact__row">sales@falconfreight.example.nz
        <svg class="contact__icon" viewBox="0 0 24 24"><path d="M2 5h20v14H2zm2 2v.5l8 5 8-5V7zm0 2.8V17h16V9.8l-8 5z"/></svg>
      </div>
      <div class="contact__address">
        <div>12-18 Kowhai Lane, Harbourvale, 9071</div>
        <div>PO Box 814, Harbourvale</div>
        <div>Northland 9072, New Zealand</div>
      </div>
    </div>
  </section>

  <section class="card card--back" aria-label="Business card back">
    <div class="brand"><span class="brand__mark"></span>Falcon Freight</div>
  </section>
</main>
</body>
</html>
```